Gym opening flyer

We need a flyer design for the opening/launch of our gym. We need the flyer ASAP. So we would like to choose the flyer as soon as possible. We will open the gym on Saturday, Feb 10. The flyer should have a front and back side

We would like to base the flyer on the following flyer (see link below) or something similar.

https://lunqo.example/img/Qw7rTz

I have also uploaded/attached our logo and pictures that we would like to use in our flyer. I have also attached a drawings of the front and back side of the flyer of what changes I would like (compared to the flyer in the link above).

You can use the text for Abour Us, Facilities from our webside www.zok.ae

Target Market(s)

Dubai, UAE

Industry/Entity Type

Fitness

Font styles to use
Other font styles liked:
• Primal

Requirements
Must have
• We need the design ASAP. We must have the Logo on the flyer and that we are opening on Feb 10th and that we have an open house between 10am to 7pm. We also need references to
• our website www.zok.ae
• Instagram @zokdubai
• Facebook @zokdubai
• Special offer that the flyer entitles the person to 3 free classes that is valid for one month until March 10, 2018.
Nice to have
• see above
Should not have
• see above

```html
<!DOCTYPE html>
<html lang="en">
<head>
<meta charset="utf-8">
<title>ZOK Dubai – Grand Opening Flyer</title>
<link rel="stylesheet" href="https://fonts.googleapis.com/css2?family=Oswald:wght@700&family=Roboto+Condensed:ital,wght@0,400;0,700;1,400;1,700&family=Roboto:wght@400&display=swap">
<style>
:root{
  --bg:#dcd9d5;
  --dark:#1c1c1c;
  --dark-2:#2c2c2c;
  --dark-3:#3d3d3d;
  --blue:#2aa4dc;
  --blue-deep:#1f78b8;
  --light:#e7e8ea;
  --white:#ffffff;
  --grey-text:#d0d0d0;
}
*{box-sizing:border-box;margin:0;padding:0}
html,body{width:1200px;height:929px;overflow:hidden}
body{background:var(--bg);font-family:"Roboto Condensed",sans-serif;color:var(--white);position:relative}

.flyer{position:absolute;top:89px;width:490px;height:757px;background:var(--dark);overflow:hidden}
.flyer--front{left:82px}
.flyer--back{left:628px}

/* shared */
.blue-rule{position:absolute;left:0;width:100%;height:3px;background:var(--blue)}
.badge{position:absolute;width:88px;height:88px;border-radius:50%;background:var(--blue);border:3px dashed var(--white);outline:4px solid var(--blue);
  display:flex;align-items:center;justify-content:center;text-align:center;transform:rotate(-18deg);
  font:700 italic 13px/1.05 "Roboto Condensed",sans-serif;text-transform:uppercase;color:var(--white)}
.brand-seal{position:absolute;width:134px;height:134px;border-radius:50%;background:var(--white);border:6px solid var(--dark);outline:3px solid var(--white);
  display:flex;align-items:center;justify-content:center;text-align:center;padding:16px;
  font:700 16px/1.15 "Roboto Condensed",sans-serif;color:var(--dark);text-transform:uppercase}
.footer-band{position:absolute;left:0;bottom:0;width:100%;height:56px;background:linear-gradient(90deg,var(--blue-deep),var(--blue) 40%,#4cb6e6);
  display:flex;align-items:center;justify-content:center}
.footer-band .site{font:400 27px/1 "Roboto",sans-serif;letter-spacing:3px;color:var(--white)}
.footer-band .dots{position:absolute;left:21px;top:19px;display:flex;gap:4px}
.footer-band .dots span{width:19px;height:19px;border-radius:50%;background:var(--white)}
.offer-band{position:absolute;left:0;top:507px;width:100%;height:70px;background:var(--light);text-align:center;color:var(--blue-deep)}
.info-panel{position:absolute;left:0;top:577px;width:100%;height:124px;background:linear-gradient(180deg,#111 0%,#2b2b2b 55%,#1a1a1a 100%)}
.panel-title{font:700 italic 20px/1 "Roboto Condensed",sans-serif;color:var(--white)}
.panel-title em{color:var(--blue);font-style:italic}

/* front */
.front-head{position:absolute;left:0;top:0;width:100%;height:285px;background:radial-gradient(circle at 70% 30%,#4a4a4a,#262626 70%)}
.front-strip{position:absolute;left:0;top:68px;width:100%;height:50px;background:#050505;border-top:3px solid var(--blue);border-bottom:3px solid var(--blue)}
.strip-label{position:absolute;top:84px;font:400 20px/1 "Roboto Condensed",sans-serif;color:var(--blue)}
.headline{position:absolute;left:21px;top:165px;font:700 italic 53px/1 "Roboto Condensed",sans-serif;color:var(--white);white-space:nowrap}
.date{position:absolute;left:21px;top:229px;font:700 italic 21px/1 "Roboto Condensed",sans-serif;color:var(--blue)}
.timetable{position:absolute;left:0;top:285px;width:100%;height:200px;background:linear-gradient(180deg,#161616,#262626)}
.timetable h2{position:absolute;left:21px;top:20px;font:400 20px/1 "Roboto Condensed",sans-serif}
.timetable ul{position:absolute;left:21px;top:58px;width:232px;list-style:none}
.timetable li{height:26.5px;padding-top:4px;border-bottom:2px dotted var(--blue);font:400 14px/1 "Roboto Condensed",sans-serif}
.timetable li span{color:var(--blue);margin-left:4px}
.athlete{position:absolute;left:283px;top:138px;width:207px;height:367px;background:linear-gradient(180deg,#5a5a5a,#2f2f2f 60%,#1a1a1a);border-radius:90px 90px 0 0}
.offer-band p{font:italic 400 16px/1.4 "Roboto Condensed",sans-serif}
.offer-band p:first-child{margin-top:14px}
.offer-band b{font-weight:700}
.about .panel-title{position:absolute;left:27px;top:16px}
.about p{position:absolute;left:27px;top:46px;width:438px;font:400 13.5px/1.55 "Roboto Condensed",sans-serif;color:var(--grey-text);text-align:justify}

/* back */
.photo-row{position:absolute;left:0;top:0;width:100%;height:157px;display:flex;gap:3px;background:var(--blue)}
.photo{flex:1;height:154px}
.photo--a{background:linear-gradient(135deg,#cfd3d6,#6d6d6d)}
.photo--b{background:linear-gradient(135deg,#c9403a,#5b5b5b)}
.photo--c{background:linear-gradient(135deg,#e2e2e2,#8a8a8a)}
.facilities{position:absolute;left:0;top:160px;width:100%;height:180px;background:radial-gradient(circle at 65% 50%,#555,#2a2a2a 75%)}
.facilities h2{position:absolute;left:27px;top:14px;font:700 italic 29px/1 "Roboto Condensed",sans-serif;color:var(--blue)}
.facilities ul{position:absolute;left:27px;top:56px;list-style:none}
.facilities li{height:31px;font:400 16px/1 "Roboto Condensed",sans-serif;display:flex;align-items:center;gap:14px}
.facilities svg{width:14px;height:12px}
.slogan{position:absolute;left:226px;top:36px;width:204px;text-align:center;font:700 40px/1.08 "Oswald",sans-serif;color:#e3e3e3;text-transform:uppercase;letter-spacing:1px}
.slogan em{font-style:normal;color:var(--blue)}
.connect{position:absolute;left:0;top:343px;width:100%;height:164px;background:linear-gradient(180deg,#1a1a1a,#2e2e2e)}
.connect h2{position:absolute;left:241px;top:18px;font:700 italic 25px/1 "Roboto Condensed",sans-serif;color:var(--blue)}
.connect ul{position:absolute;left:243px;top:56px;list-style:none}
.connect li{height:31.5px;display:flex;align-items:center;gap:14px;font:400 17px/1 "Roboto Condensed",sans-serif}
.connect li span.dot{width:20px;height:20px;border-radius:50%;background:var(--white)}
.cta{font:700 italic 22px/1.35 "Roboto Condensed",sans-serif;letter-spacing:2.5px;text-transform:uppercase;padding-top:10px}
.contact{text-align:center}
.contact .panel-title{margin-top:15px}
.contact p{font:400 13.5px/1.6 "Roboto Condensed",sans-serif;color:var(--white);margin-top:8px}
</style>
</head>
<body>

<!-- FRONT -->
<section class="flyer flyer--front" aria-label="Flyer front">
  <div class="front-head"></div>
  <div class="front-strip"></div>
  <span class="strip-label" style="left:112px">ZOK</span>
  <span class="strip-label" style="left:345px">DUBAI</span>
  <div class="athlete" role="img" aria-label="Photo of a female athlete holding a dumbbell"></div>
  <div class="brand-seal" style="left:176px;top:26px">Zenith Origin Kinetics</div>
  <div class="badge" style="left:15px;top:14px">All<br>Ages<br>Welcome</div>
  <h1 class="headline">Grand Opening</h1>
  <p class="date">Saturday 10th February</p>
  <div class="blue-rule" style="top:282px"></div>
  <div class="timetable">
    <h2>Grand Opening Timetable</h2>
    <ul>
      <li>10am <span>Gym Opens</span></li>
      <li>11am <span>Power Drill</span></li>
      <li>1pm <span>Body Fit</span></li>
      <li>3pm <span>Calorie Burn</span></li>
      <li>7pm <span>Gym Closed</span></li>
    </ul>
  </div>
  <div class="blue-rule" style="top:484px;width:283px"></div>
  <div class="offer-band">
    <p><b>Special Offer</b> - Mention This Flyer and receive <b>3 Free Classes</b></p>
    <p>that is valid for one month until March 10, 2018.</p>
  </div>
  <div class="info-panel about">
    <h2 class="panel-title">About <em>US</em></h2>
    <p>Zenith Origin Kinetics is a gym focused on circuit style training for all levels of fitness. We provide engaging and motivating group exercise classes that are both challanging and fun.</p>
  </div>
  <div class="footer-band">
    <div class="dots"><span></span><span></span></div>
    <span class="site">www.ZOK.ae</span>
  </div>
</section>

<!-- BACK -->
<section class="flyer flyer--back" aria-label="Flyer back">
  <div class="photo-row">
    <div class="photo photo--a" role="img" aria-label="Photo of athlete training with a medicine ball"></div>
    <div class="photo photo--b" role="img" aria-label="Photo of a group class jumping in the studio"></div>
    <div class="photo photo--c" role="img" aria-label="Photo of athlete working with battle ropes"></div>
  </div>
  <div class="facilities">
    <h2>Facilities</h2>
    <ul>
      <li><svg viewBox="0 0 14 12"><path d="M1 6l4 4 8-9" fill="none" stroke="#2aa4dc" stroke-width="2"/></svg>Indoor Studio</li>
      <li><svg viewBox="0 0 14 12"><path d="M1 6l4 4 8-9" fill="none" stroke="#2aa4dc" stroke-width="2"/></svg>Outdoor Terrace</li>
      <li><svg viewBox="0 0 14 12"><path d="M1 6l4 4 8-9" fill="none" stroke="#2aa4dc" stroke-width="2"/></svg>Locker Rooms</li>
      <li><svg viewBox="0 0 14 12"><path d="M1 6l4 4 8-9" fill="none" stroke="#2aa4dc" stroke-width="2"/></svg>Lounge Area</li>
    </ul>
    <p class="slogan">Wake up<br>it's time<br>to <em>lift</em></p>
  </div>
  <div class="blue-rule" style="top:157px"></div>
  <div class="blue-rule" style="top:340px"></div>
  <div class="badge" style="left:393px;top:122px">All<br>Ages<br>Welcome</div>
  <div class="connect">
    <h2>Check Us Out On:</h2>
    <ul>
      <li><span class="dot"></span>@zokdubai</li>
      <li><span class="dot"></span>@zokdubai</li>
      <li><span class="dot"></span>www.zok.ae</li>
    </ul>
  </div>
  <div class="brand-seal" style="left:39px;top:356px">Zenith Origin Kinetics</div>
  <div class="offer-band cta">
    See Classes / Timetable / Pricing<br>www.zok.ae
  </div>
  <div class="info-panel contact">
    <h2 class="panel-title">Contact <em>US</em></h2>
    <p>+971501234567<br>info@zok.ae<br>Sahar House 12th Floor - Crescent Heights - Dubai - United Arab Emirates</p>
  </div>
  <div class="footer-band">
    <div class="dots"><span></span><span></span></div>
    <span class="site">www.ZOK.ae</span>
  </div>
</section>

</body>
</html>
```